Wordpress Design Project

I need a wordpress design for a new business called the Skyvale Personal Development Center. We offer online and live self improvement programs and seminars that utilize self hypnosis.. I have a logo that I want the design built around, file is attached (I don't have a problem with you moving the logo words around, I just want to keep same design, font, colors)

The completed project will be the design and code for a child theme for the meridian framework. This will include the home page design and 3 separate subpage variation designs based on the main theme.

The design should communicate growth, potential and success.

Target Market(s)

70% women, well educated, open to alternative

Industry/Entity Type

Business

Requirements
Must have
• A key part of this design is having an effective optin box located on the right side. The main goal of this site is to get people to optin to my email list followed by easy navigation to different programs and content that are on the site.

```html
<!DOCTYPE html>
<html lang="en">
<head>
<meta charset="utf-8">
<title>Skyvale Personal Development Center</title>
<link href="https://fonts.googleapis.com/css2?family=PT+Sans:wght@400;700&display=swap" rel="stylesheet">
<style>
:root{
  --purple:#6a2d86;
  --purple-dark:#4a1858;
  --purple-text:#5b2a80;
  --hero-top:#8e44a3;
  --hero-bottom:#5c2270;
  --navy:#2b2d85;
  --navy-light:#3d3f9c;
  --orange:#f39a1b;
  --ink:#222;
  --body:#6b6b6b;
  --muted:#8a8a8a;
  --rule:#e2e2e2;
  --white:#fff;
}
*{margin:0;padding:0;box-sizing:border-box}
html,body{width:804px;height:1200px;overflow:hidden;background:var(--white)}
body{position:relative;font-family:"PT Sans",Arial,sans-serif;color:var(--ink)}
.abs{position:absolute}

/* header */
.topline{left:0;top:0;width:804px;height:3px;background:#ececec}
.account-btn{top:3px;height:19px;background:#e3e3e3;color:#666;font-size:9.5px;line-height:19px;text-align:center;border-radius:0 0 3px 3px}
.brand-mark{left:52px;top:21px;width:56px;height:56px;border-radius:50%;border:4px solid var(--purple)}
.brand-name{left:116px;top:30px;width:130px;color:var(--purple);font-size:13px;font-weight:700;line-height:14px}
.main-nav{right:63px;top:52px;display:flex;font-size:13px;color:var(--purple-text)}
.main-nav span{padding:0 13px;border-left:1px solid #ccc;line-height:13px}
.main-nav span:first-child{border-left:none}
.main-nav span:last-child{padding-right:0}

/* hero */
.hero{left:0;top:86px;width:804px;height:300px;background:linear-gradient(180deg,var(--hero-top),var(--hero-bottom))}
.hero-kicker{left:67px;top:131px;color:var(--white);font-size:22px;font-weight:400}
.hero-title{left:67px;top:151px;color:var(--white);font-size:32px;font-weight:400}
.hero-sub{left:68px;top:195px;color:#f1e6f5;font-size:14px}
.hero-copy{left:68px;top:214px;width:285px;color:#ead9f0;font-size:9.5px;line-height:15px}
.btn{top:271px;height:25px;font-size:10px;font-weight:700;line-height:25px;text-align:center;border-radius:3px}
.btn-register{left:68px;width:94px;background:var(--white);color:var(--purple-dark)}
.btn-learn{left:169px;width:83px;background:var(--purple-dark);color:var(--white)}
.slider-dots{left:71px;top:322px;display:flex;gap:3px}
.slider-dots i{width:6px;height:6px;border-radius:50%;background:#b590c3}
.slider-dots i:first-child{background:var(--white)}
.hero-frame{left:387px;top:112px;width:352px;height:239px;background:#b47fc7}
.hero-photo{left:394px;top:119px;width:338px;height:226px;background:linear-gradient(160deg,#f4f4f4,#d8dadf 60%,#b9a0a0)}

/* features */
.feature-title{top:414px;color:var(--purple-text);font-size:14.5px}
.feature-photo{top:437px;width:214px;height:93px;border:1px solid #ddd}
.feature-sub{top:539px;font-size:10px;color:var(--ink)}
.feature-copy{top:558px;width:210px;font-size:8.6px;line-height:15.2px;color:var(--body);text-align:justify}
.learn-more{top:609px;font-size:9px;color:#444}
.learn-more::after{content:"";display:inline-block;margin-left:3px;border-left:4px solid #666;border-top:3px solid transparent;border-bottom:3px solid transparent}
.divider{left:51px;top:645px;width:703px;height:1px;background:var(--rule)}

/* welcome */
.welcome-title{left:54px;top:671px;font-size:15px;color:var(--ink)}
.welcome-lead{left:54px;top:697px;font-size:10px;color:var(--navy)}
.welcome-copy{left:54px;width:490px;font-size:8.6px;line-height:15.2px;color:var(--body)}
.classes-title{left:52px;top:842px;font-size:13px;color:var(--ink)}
.class-photo{top:870px;width:151px;height:98px;border-radius:3px}
.class-name{top:976px;font-size:9px;color:var(--ink)}
.class-copy{top:991px;width:145px;font-size:8.6px;line-height:15.2px;color:var(--body)}

/* sidebar */
.side-box{border:1px solid #e4e4e4;border-radius:2px;background:var(--white)}
.side-head{left:0;top:0;right:0;height:32px;color:var(--white);font-size:12px;font-weight:700;line-height:32px;padding-left:14px}
.optin-head{background:linear-gradient(180deg,var(--navy-light),var(--navy))}
.testi-head{background:linear-gradient(180deg,#7a3a96,var(--hero-bottom))}
.optin-text{left:13px;top:45px;font-size:8.4px;color:#444}
.optin-input{left:12px;top:59px;width:163px;height:21px;border:1px solid #d6d6d6;font-size:8.4px;color:#888;line-height:20px;padding-left:8px}
.optin-btn{left:110px;top:87px;width:65px;height:21px;background:var(--orange);color:var(--white);font-size:9px;font-weight:700;line-height:21px;text-align:center;border-radius:2px}
.quote{left:19px;width:150px;font-size:8.3px;line-height:13.8px;color:var(--muted)}
.quote-author{left:19px;font-size:10px;color:#444}

/* footer */
.footer{left:0;top:1088px;width:804px;height:112px;background:linear-gradient(180deg,#ececec,#f7f7f7 12px,#fbfbfb)}
.footer-nav{left:54px;top:1114px;display:flex;font-size:10px;color:#444}
.footer-nav span{padding:0 7px;border-left:1px solid #555;line-height:10px}
.footer-nav span:first-child{padding-left:0;border-left:none}
.copyright{left:54px;top:1142px;font-size:7.5px;color:#666}
.social{left:664px;top:1114px;display:flex;gap:5px}
.social i{width:16px;height:16px;border-radius:2px}
</style>
</head>
<body>

<header>
  <div class="abs topline"></div>
  <div class="abs account-btn" style="left:622px;width:44px">Log In</div>
  <div class="abs account-btn" style="left:674px;width:56px">Register</div>
  <div class="abs brand-mark"></div>
  <div class="abs brand-name">Skyvale Personal Development Center</div>
  <nav class="abs main-nav">
    <span>Main</span><span>About Us</span><span>Training</span><span>Join Us</span><span>Services</span><span>Contact</span>
  </nav>
</header>

<section class="abs hero"></section>
<div class="abs hero-kicker">Want to Improve</div>
<div class="abs hero-title">Your Personality</div>
<div class="abs hero-sub">JOIN SKYVALE CENTER NOW</div>
<p class="abs hero-copy">Maecenas aliquet velit vel turpis. Mauris neque metus, malesuada nec, ultricies sit amet, porttitor mattis, enim. In massa libero, interdum nec, interdum vel, blandit sed, nulla.</p>
<div class="abs btn btn-register">REGISTER NOW</div>
<div class="abs btn btn-learn">LEARN MORE</div>
<div class="abs slider-dots"><i></i><i></i><i></i><i></i></div>
<div class="abs hero-frame"></div>
<div class="abs hero-photo" role="img" aria-label="Seminar room with an audience seated in red chairs applauding a presenter at a flip chart"></div>

<section>
  <h2 class="abs feature-title" style="left:58px">Why Personality Development</h2>
  <h2 class="abs feature-title" style="left:297px">Seminars &amp; Training</h2>
  <h2 class="abs feature-title" style="left:534px">Online Programs</h2>

  <div class="abs feature-photo" style="left:57px;background:linear-gradient(90deg,#e9d3c3,#a9b4c4 60%,#c9c1bf)" role="img" aria-label="Group of smiling students in a classroom"></div>
  <div class="abs feature-photo" style="left:296px;background:linear-gradient(90deg,#c9c6bf,#7f8a4f 45%,#d7cfc6)" role="img" aria-label="Young man in a seminar audience"></div>
  <div class="abs feature-photo" style="left:533px;background:linear-gradient(90deg,#e4e2e0,#c2c6cc 55%,#f2f2f2)" role="img" aria-label="People working together on a laptop"></div>

  <div class="abs feature-sub" style="left:59px">Pellentesque habitant morbi tristique</div>
  <div class="abs feature-sub" style="left:297px">Mauris vel lacus vitae felis vestibulum</div>
  <div class="abs feature-sub" style="left:534px">Nunc tempus felis vitae urna</div>

  <p class="abs feature-copy" style="left:59px">Offsite Backup should be the key driver in any business continuity plan, but it doesn't have to come with a price tag suitable only for large conglomerates.</p>
  <p class="abs feature-copy" style="left:297px">Offsite Backup should be the key driver in any business continuity plan, but it doesn't have to come with a price tag suitable only for large conglomerates.</p>
  <p class="abs feature-copy" style="left:534px">Offsite Backup should be the key driver in any business continuity plan, but it doesn't have to come with a price tag suitable only for large conglomerates.</p>

  <div class="abs learn-more" style="left:60px">Learn More</div>
  <div class="abs learn-more" style="left:297px">Learn More</div>
  <div class="abs learn-more" style="left:535px">Learn More</div>
</section>

<div class="abs divider"></div>

<main>
  <h1 class="abs welcome-title">Welcome to Brightpath Website Mainpage..</h1>
  <div class="abs welcome-lead">Nam cursus. Morbi ut mi. Nullam enim leo, egestas id, condimentum at, laoreet mattis, massa.</div>
  <p class="abs welcome-copy" style="top:715px">Phasellus felis dolor, scelerisque a, tempus eget, lobortis id, libero. Donec scelerisque leo ac risus. Praesent sit amet est. In dictum, dolor eu dictum porttitor, enim felis viverra mi, eget luctus massa purus quis odio. Etiam nulla massa, pharetra facilisis, volutpat in, imperdiet sit amet, sem. Aliquam nec erat at purus cursus interdum. Vestibulum ligula augue, bibendum accumsan, vestibulum ut, commodo a, mi. Morbi ornare gravida elit. Integer congue, augue et malesuada iaculis.</p>
  <p class="abs welcome-copy" style="top:783px">Aliquet felis, at cursus magna nisl nec elit. Donec iaculis diam a nisi accumsan viverra. Duis sed tellus et tortor vestibulum gravida. Praesent elementum elit at tellus. Curabitur metus ipsum, luctus eu, malesuada ut, tincidunt sed, diam.</p>

  <h2 class="abs classes-title">Some of Our Development Classes</h2>
  <div class="abs class-photo" style="left:50px;background:linear-gradient(90deg,#e6e6e3,#9aa3ad 50%,#ecebe6)" role="img" aria-label="Teacher explaining a diagram on a whiteboard to a student"></div>
  <div class="abs class-photo" style="left:217px;background:linear-gradient(90deg,#c8ccd2,#6d7178 50%,#d9c27a)" role="img" aria-label="Students working together at computers"></div>
  <div class="abs class-photo" style="left:382px;background:linear-gradient(90deg,#dfe6ee,#a8bfd6 45%,#e9e4de)" role="img" aria-label="Instructor speaking to a raised-hand audience"></div>

  <div class="abs class-name" style="left:53px">Aliquet felis at cursus</div>
  <div class="abs class-name" style="left:223px">Aliquet felis at cursus</div>
  <div class="abs class-name" style="left:387px">Aliquet felis at cursus</div>
  <p class="abs class-copy" style="left:53px">Donec iaculis diam a nisi accumsan viverra. Duis sed tellus et tortor vestibulum gravida.</p>
  <p class="abs class-copy" style="left:223px">Donec iaculis diam a nisi accumsan viverra. Duis sed tellus et tortor vestibulum gravida.</p>
  <p class="abs class-copy" style="left:387px">Donec iaculis diam a nisi accumsan viverra. Duis sed tellus et tortor vestibulum gravida.</p>
</main>

<aside>
  <div class="abs side-box" style="left:564px;top:670px;width:187px;height:124px">
    <div class="abs side-head optin-head">Newsletters Sign up</div>
    <div class="abs optin-text">Please sign up here for latest newsletters.</div>
    <div class="abs optin-input">email address</div>
    <div class="abs optin-btn">SUBSCRIBE</div>
  </div>

  <div class="abs side-box" style="left:564px;top:806px;width:187px;height:254px">
    <div class="abs side-head testi-head">Students Testimonials</div>
    <p class="abs quote" style="top:47px">Nunc tempus felis vitae urna. Vivamus porttitor purus nisl eleifend libero, a tempus libero lectus feugiat felis. Morbi diam mauris, viverra in, gravida eu, mattis in ante.</p>
    <div class="abs quote-author" style="top:119px">By Author Name</div>
    <p class="abs quote" style="top:147px">Nunc tempus felis vitae urna. Vivamus porttitor purus nisl eleifend libero, a tempus libero lectus feugiat felis. Morbi diam mauris, viverra in, gravida eu, mattis in ante.</p>
    <div class="abs quote-author" style="top:219px">By Author Name</div>
  </div>
</aside>

<footer>
  <div class="abs footer"></div>
  <nav class="abs footer-nav">
    <span>Main</span><span>About Us</span><span>Training</span><span>Join Us</span><span>Services</span><span>Contact</span>
  </nav>
  <div class="abs copyright">Copyright © 2013 Company Name.&nbsp; All right reserved.&nbsp; Term of Use</div>
  <div class="abs social">
    <i style="background:#3b5998"></i><i style="background:#0e76a8"></i><i style="background:#f08a24"></i><i style="background:#c4302b"></i>
  </div>
</footer>

</body>
</html>
```